Instant Broth for Ramen and Soup - Need labels for three flavors

We are a new company planning to launch a line of all natural powdered instant broth for ramen and soups. We need a logo design for our three launch flavors which will be Chicken, Prime Beef and Garden Vegetable. The powdered broth will be sold in 4oz containers with a white cap.
We would like the logo to be at the top of the label and or product description "Instant Broth for Ramen and Soups" underneath. The product description should stand out to the consumer, so it should likely be a larger font and one that compliments the logo. Below the Product description, we would like the name of the flavor and appropriate color scheme to match the flavor (see product picture for color). The design for each flavor should be the same, the only thing that should change is the color scheme to match flavor. Because we use all natural ingredients we would also like the label to state "Natural Ingredients" and "Gluten Free" on the front.
Additionally if you could please include placeholders for the nutritional label, ingredients list beneath, net size/weight on the side, bar code and a placeholder address for "Veltmore Foods LLC" that would be great as we are still finalizing these details. We would also like the label design to be catchy and interesting while complimenting the fun light-hearted logo.
Lastly, if your design is chosen you will be our main choice for additional design work (if you wish) including, top label design for the cap, finalizing the product info, formatting actual jar dimensions and other design work for the many other additional flavors we will be releasing.
Target Market(s)
Homemade ramen and soup connoisseurs, health conscious consumers, millennials and college students
Industry/Entity Type
It Company
Other font styles liked:
- SingleSleeve
Colors
Designer to choose colors to be used in the design.
Requirements
Must have
- 1) Logo
- 2) Product description "Instant Broth for Ramen and Soups"
- 3) Flavor title and color scheme
- 4) "Natural Ingredients" and "Gluten Free"
- 5) Place holder info for FDA required information (nutrition facts, net weight etc.)
Nice to have
- 1) Instructions (placeholder)
- 2) Additional info about the product (placeholder)

```html
<!DOCTYPE html>
<html lang="en">
<head>
<meta charset="utf-8">
<title>Simmera Garden Vegetable Label</title>
<link rel="stylesheet" href="https://fonts.googleapis.com/css2?family=Amatic+SC:wght@400;700&family=Arimo:wght@400;700&family=Oswald:wght@500&display=swap">
<style>
  :root {
    --page-bg: #1e1e1e;
    --band-green: rgba(44, 74, 50, 0.92);
    --white: #ffffff;
    --panel-shade: rgba(70, 70, 70, 0.55);
    --ink: #111111;
  }
  * { box-sizing: border-box; margin: 0; padding: 0; }
  html, body { width: 1200px; height: 1200px; overflow: hidden; background: var(--page-bg); }
  .canvas { position: relative; width: 1200px; height: 1200px; }
  .label {
    position: absolute; left: 0; top: 402px; width: 1200px; height: 396px; overflow: hidden;
  }
  .label__photo {
    position: absolute; inset: 0;
    background:
      linear-gradient(180deg, rgba(0,0,0,0) 55%, rgba(60,40,25,0.9) 70%, rgba(70,50,35,1) 100%),
      linear-gradient(90deg, #3d5a2e 0%, #5a7a3a 12%, #b07a4e 26%, #a9774d 36%, #c9572a 48%, #d8633a 56%, #c9a02a 68%, #d4b22a 78%, #8a6a4a 90%, #6b4a32 100%);
  }
  .logo-disc {
    position: absolute; left: 520px; top: -12px; width: 170px; height: 100px;
    border-radius: 0 0 85px 85px; background: rgba(255,255,255,0.28);
  }
  .brand-name {
    position: absolute; left: 0; width: 1200px; top: 28px; text-align: center;
    font-family: "Oswald", sans-serif; font-weight: 500; font-size: 34px; color: var(--white); letter-spacing: 1px;
  }
  .flavor-band {
    position: absolute; left: 0; top: 144px; width: 996px; height: 110px; background: var(--band-green);
  }
  .tagline {
    position: absolute; left: 430px; width: 340px; top: 154px; text-align: center;
    border-top: 1px solid var(--white); border-bottom: 1px solid var(--white);
    font-family: "Amatic SC", sans-serif; font-size: 26px; line-height: 30px; color: var(--white); letter-spacing: 2px;
  }
  .flavor-name {
    position: absolute; left: 0; width: 1200px; top: 186px; text-align: center;
    font-family: "Oswald", sans-serif; font-weight: 500; font-size: 52px; line-height: 60px;
    color: var(--white); transform: scaleX(0.8); letter-spacing: 1px;
  }
  .claims {
    position: absolute; left: 0; width: 1200px; top: 324px; text-align: center;
    font-family: "Amatic SC", sans-serif; font-size: 24px; line-height: 22px; color: var(--white); letter-spacing: 2px;
  }
  .claims .net { font-family: "Arimo", sans-serif; font-size: 17px; letter-spacing: 0; line-height: 26px; }
  .info-panel {
    position: absolute; background: var(--panel-shade); color: var(--white); padding: 6px 8px;
  }
  .info-panel h3 {
    font-family: "Amatic SC", sans-serif; font-weight: 400; font-size: 26px; letter-spacing: 2px; line-height: 28px;
  }
  .info-panel p { font-family: "Arimo", sans-serif; font-size: 13.5px; line-height: 17px; }
  .instructions { left: 11px; top: 263px; width: 197px; height: 119px; }
  .instructions svg { position: absolute; left: 60px; top: 72px; }
  .ingredients { left: 996px; top: 302px; width: 192px; height: 88px; }
  .nutrition {
    position: absolute; left: 996px; top: 8px; width: 194px; height: 290px; background: var(--white);
    border: 1.5px solid var(--ink); padding: 2px 3px; font-family: "Arimo", sans-serif; color: var(--ink); font-size: 9.5px;
  }
  .nutrition h2 { font-size: 25px; font-weight: 700; line-height: 28px; letter-spacing: -0.3px; }
  .nutrition .row { display: flex; justify-content: space-between; border-top: 1px solid var(--ink); line-height: 15px; }
  .nutrition .thick { border-top: 6px solid var(--ink); }
  .nutrition .mid { border-top: 3px solid var(--ink); }
  .nutrition .indent { padding-left: 16px; }
  .nutrition .small { font-size: 7px; }
  .nutrition b { font-weight: 700; }
  .nutrition .note { font-size: 7.5px; line-height: 9px; border-top: 1px solid var(--ink); margin-top: 24px; padding-top: 2px; }
</style>
</head>
<body>
<div class="canvas">
  <section class="label">
    <div class="label__photo" role="img" aria-label="Photo of ground spices and dried herbs in white spoons on a wooden table with star anise and dried chili"></div>
    <div class="logo-disc"></div>
    <div class="brand-name">SIMMERA</div>

    <div class="flavor-band"></div>
    <div class="tagline">INSTANT BROTH FOR RAMEN AND SOUPS</div>
    <div class="flavor-name">GARDEN VEGETABLE</div>

    <div class="claims">GLUTEN FREE<br>NATURAL INGREDIENTS<br><span class="net">4 oz</span></div>

    <div class="info-panel instructions">
      <h3>INSTRUCTIONS:</h3>
      <p>Mix 1 teaspoon in 1 cup of water, I would guess.</p>
      <svg width="90" height="42" viewBox="0 0 90 42" aria-hidden="true">
        <path d="M2 12 h40 v22 q0 6 -6 6 h-28 q-6 0 -6 -6 z" fill="rgba(255,255,255,0.55)"/>
        <ellipse cx="54" cy="6" rx="7" ry="3.5" fill="rgba(255,255,255,0.55)"/>
        <rect x="58" y="4.5" width="26" height="2.5" rx="1.2" fill="rgba(255,255,255,0.55)"/>
      </svg>
    </div>

    <div class="nutrition">
      <h2>Nutrition Facts</h2>
      <div>Serving Size 1 tsp (5g)</div>
      <div>Servings Per Container 10</div>
      <div class="row thick small"><b>Amount Per Serving</b></div>
      <div class="row"><span><b>Calories</b> 150</span><span>Calories from Fat 20</span></div>
      <div class="row mid small" style="justify-content:flex-end"><b>% Daily Value*</b></div>
      <div class="row"><span><b>Total Fat</b> 3.5g</span><b>5%</b></div>
      <div class="row indent"><span>Saturated Fat 1g</span><b>5%</b></div>
      <div class="row"><span><b>Sodium</b> 0mg</span><b>10%</b></div>
      <div class="row"><span><b>Total Carbohydrate</b> 33mg</span><b>20%</b></div>
      <div class="row indent"><span>Dietary Fiber 6g</span><b>50%</b></div>
      <div class="row"><span><b>Protein</b> 10g</span></div>
      <div class="row thick"><span>Vitamin C &nbsp; 2% &nbsp;&nbsp;&nbsp;&nbsp;&nbsp;&nbsp;&nbsp;&nbsp; •</span><span>Calcium 8%</span></div>
      <div class="row"><span>Iron 30%</span></div>
      <div class="note">*Percent Daily Values are based on a 2,000 calorie diet.</div>
    </div>

    <div class="info-panel ingredients">
      <h3>INGREDIENTS:</h3>
      <p>Water, vegetables, from your garden, things, water.</p>
    </div>
  </section>
</div>
</body>
</html>
```